Transform this table

Please make a 2 page A4 handout from this boring table into an engaging design. The front page can be simple and engaging (a summary of the back where all the detail lives)

Target Market(s)

Business

Requirements
Must have
• Clarity. And impact.
Nice to have
• Icons

```html
<!DOCTYPE html>
<html lang="en">
<head>
<meta charset="utf-8">
<title>Safety Culture Maturity Ladder</title>
<link rel="stylesheet" href="https://fonts.googleapis.com/css2?family=Bebas+Neue&family=Oswald:wght@300;400;600;700&family=Roboto:wght@400;700&display=swap">
<style>
  :root {
    --backdrop: #a4a4a4;
    --navy: #1d2f66;
    --navy-deep: #15234f;
    --navy-light: #2e4a8e;
    --lime: #cfdc00;
    --green: #5db52c;
    --orange: #ee8a10;
    --yellow: #f4c300;
    --red: #e8543a;
    --red-bar: #e8402a;
    --bracket: #5b86c7;
    --ink: #2b2b2b;
    --paper: #ffffff;
  }
  * { box-sizing: border-box; }
  html, body { margin: 0; padding: 0; }
  body {
    width: 861px; height: 1200px; overflow: hidden;
    background: var(--backdrop);
    position: relative;
    font-family: "Roboto", Arial, sans-serif;
  }
  .page {
    position: absolute; left: 67px; width: 714px; height: 504px;
    background: var(--paper); overflow: hidden;
  }
  .page-summary { top: 62px; }
  .page-detail { top: 631px; }
  .page svg { position: absolute; left: 0; top: 0; width: 714px; height: 504px; }

  .title { font-family: "Bebas Neue", "Oswald", sans-serif; }
  .level-label { font-family: "Bebas Neue", "Oswald", sans-serif; fill: #111; }
  .level-quote { font-family: "Roboto", Arial, sans-serif; fill: #1a1a1a; }
  .side-note { font-family: "Oswald", Arial, sans-serif; font-weight: 300; fill: #222; font-size: 15px; }
  .axis-text { font-family: "Oswald", Arial, sans-serif; font-weight: 600; fill: var(--navy); font-size: 19px; }
  .source-line { font-family: "Bebas Neue", "Oswald", sans-serif; fill: var(--navy); font-size: 34px; }

  /* detail page */
  .culture-col {
    position: absolute; top: 20px; width: 126px;
    font-size: 7.3px; line-height: 1.12; color: var(--ink);
  }
  .culture-col h3 {
    position: relative; margin: 0 0 5px; padding-left: 11px;
    font-size: 7.5px; font-weight: 700; line-height: 1.15;
  }
  .culture-col ul, .practice-col ul { list-style: none; margin: 0; padding: 0; }
  .culture-col li, .practice-col li { position: relative; padding-left: 11px; margin-bottom: 4.6px; }
  .culture-col h3::before, .culture-col li::before, .practice-col li::before {
    content: "✓"; position: absolute; left: 0; top: 0.5px;
    width: 6.5px; height: 6.5px; border-radius: 50%;
    font-size: 4.6px; line-height: 6.5px; text-align: center; font-weight: 700;
    background: var(--red); color: #fff;
  }
  .culture-col ul.traits { margin: 0 0 7px; }
  .culture-col ul.traits li { padding-left: 22px; }
  .culture-col ul.traits li::before {
    left: 11px; background: none; border: 0.8px solid var(--orange); color: var(--orange); line-height: 5px;
  }
  .culture-col li.lead { font-weight: 700; }
  .outcome {
    position: absolute; background: var(--red-bar); color: #fff;
    font-size: 7px; font-weight: 700; line-height: 1.1; text-align: center; padding: 2px 3px;
  }
  .practice-col {
    position: absolute; width: 128px; color: #fff;
    font-size: 7.3px; line-height: 1.1;
  }
  .practice-col li { margin-bottom: 5.6px; }
  .practice-col li::before { background: var(--lime); color: var(--navy); }
  .practice-col li.key { color: var(--lime); font-weight: 700; }
  .practice-col ul.traits li { padding-left: 22px; }
  .practice-col ul.traits li::before { left: 11px; background: none; border: 0.8px solid var(--lime); color: var(--lime); line-height: 5px; }
  .badge-label { font-family: "Oswald", Arial, sans-serif; font-weight: 600; font-size: 15px; fill: #111; }
</style>
</head>
<body>

<!-- Front: the ladder summary -->
<section class="page page-summary">
  <svg viewBox="0 0 995 702" xmlns="http://www.w3.org/2000/svg">
    <defs>
      <linearGradient id="headerFill" x1="0" y1="0" x2="0" y2="1">
        <stop offset="0" stop-color="#2c4889"/>
        <stop offset="1" stop-color="#1a2b5f"/>
      </linearGradient>
      <linearGradient id="paperFill" x1="0" y1="0" x2="1" y2="1">
        <stop offset="0" stop-color="#e9ebee"/>
        <stop offset="0.5" stop-color="#ffffff"/>
        <stop offset="1" stop-color="#f3f4f6"/>
      </linearGradient>
      <linearGradient id="cornerFill" x1="0" y1="0" x2="1" y2="1">
        <stop offset="0" stop-color="#2a3f7a"/>
        <stop offset="0.6" stop-color="#8fa23a"/>
        <stop offset="1" stop-color="#cfdc00" stop-opacity="0.15"/>
      </linearGradient>
      <linearGradient id="tierGreen" gradientUnits="userSpaceOnUse" x1="70" y1="0" x2="772" y2="0">
        <stop offset="0" stop-color="#7cc94a"/><stop offset="0.45" stop-color="#5db52c"/><stop offset="1" stop-color="#4fa323"/>
      </linearGradient>
      <linearGradient id="tierLime" gradientUnits="userSpaceOnUse" x1="70" y1="0" x2="772" y2="0">
        <stop offset="0" stop-color="#dfe83a"/><stop offset="0.45" stop-color="#cfdc00"/><stop offset="1" stop-color="#c2cf00"/>
      </linearGradient>
      <linearGradient id="tierOrange" gradientUnits="userSpaceOnUse" x1="70" y1="0" x2="772" y2="0">
        <stop offset="0" stop-color="#f5a23a"/><stop offset="0.45" stop-color="#ee8a10"/><stop offset="1" stop-color="#e47f08"/>
      </linearGradient>
      <linearGradient id="tierYellow" gradientUnits="userSpaceOnUse" x1="70" y1="0" x2="772" y2="0">
        <stop offset="0" stop-color="#f9d43c"/><stop offset="0.45" stop-color="#f4c300"/><stop offset="1" stop-color="#ecb900"/>
      </linearGradient>
      <linearGradient id="tierRed" gradientUnits="userSpaceOnUse" x1="70" y1="0" x2="772" y2="0">
        <stop offset="0" stop-color="#ef6c55"/><stop offset="0.45" stop-color="#e8543a"/><stop offset="1" stop-color="#e04a31"/>
      </linearGradient>
    </defs>

    <rect class="paper" x="0" y="110" width="995" height="592" fill="url(#paperFill)"/>
    <rect class="header-band" x="0" y="0" width="995" height="110" fill="url(#headerFill)"/>
    <text class="title" x="497" y="93" text-anchor="middle" font-size="94" textLength="905" lengthAdjust="spacingAndGlyphs"><tspan fill="#fff">SAFETY </tspan><tspan fill="var(--lime)">CULTURE MATURITY </tspan><tspan fill="#fff">LADDER</tspan></text>

    <polygon class="corner-decoration" points="0,110 215,110 0,395" fill="url(#cornerFill)" opacity="0.55" role="img" aria-label="Diagonal navy and lime stripe decoration"/>

    <!-- axis arrow -->
    <line x1="40" y1="540" x2="250" y2="160" stroke="var(--bracket)" stroke-width="3"/>
    <polygon points="258,146 238,162 254,170" fill="var(--bracket)"/>
    <text class="axis-text" transform="translate(68,430) rotate(-57)">IMPROVING SAFETY CULTURE</text>
    <text class="axis-text" transform="translate(70,540) rotate(-60.5)">INCREASING ACCOUNTABILITY &amp; REALIABILITY</text>

    <!-- ladder levels -->
    <g class="level level-resilient">
      <rect x="380" y="132" width="392" height="88" fill="url(#tierGreen)"/>
      <polygon points="344,140 298,220 400,220" fill="url(#tierGreen)"/>
      <circle cx="344" cy="172" r="14" fill="#fff" stroke="#3f8a1d" stroke-width="2" role="img" aria-label="Resilient level icon"/>
      <text class="level-label" x="344" y="210" text-anchor="middle" font-size="21">RESILIENT</text>
      <text class="level-quote" x="760" y="175" text-anchor="end" font-size="21">Interdependent culture</text>
      <text class="level-quote" x="760" y="203" text-anchor="end" font-size="21">“It’s how we do business.”</text>
    </g>
    <g class="level level-proactive">
      <rect x="400" y="234" width="372" height="90" fill="url(#tierLime)"/>
      <polygon points="296,224 392,224 448,322 240,322" fill="url(#tierLime)"/>
      <circle cx="290" cy="268" r="16" fill="#fff" stroke="#a5b000" stroke-width="2" role="img" aria-label="Proactive level icon"/>
      <text class="level-label" x="316" y="282" font-size="32">PROACTIVE</text>
      <text class="level-quote" x="760" y="271" text-anchor="end" font-size="21">Ownership culture</text>
      <text class="level-quote" x="760" y="299" text-anchor="end" font-size="21">“We prevent incidents”</text>
    </g>
    <g class="level level-compliant">
      <rect x="460" y="330" width="312" height="90" fill="url(#tierOrange)"/>
      <polygon points="240,326 448,326 504,420 184,420" fill="url(#tierOrange)"/>
      <circle cx="256" cy="372" r="20" fill="#fff" stroke="#c96d05" stroke-width="3" role="img" aria-label="Compliant level icon"/>
      <text class="level-label" x="290" y="390" font-size="50">COMPLIANT</text>
      <text class="level-quote" x="760" y="371" text-anchor="end" font-size="21">Compliance culture</text>
      <text class="level-quote" x="760" y="399" text-anchor="end" font-size="21">“Incidents have causes”</text>
    </g>
    <g class="level level-reactive">
      <rect x="520" y="430" width="252" height="90" fill="url(#tierYellow)"/>
      <polygon points="184,424 504,424 562,520 128,520" fill="url(#tierYellow)"/>
      <circle cx="226" cy="470" r="30" fill="#fff" stroke="#c99a00" stroke-width="3" role="img" aria-label="Reactive level icon"/>
      <text class="level-label" x="276" y="498" font-size="76">REACTIVE</text>
      <text class="level-quote" x="760" y="469" text-anchor="end" font-size="21">Blame culture</text>
      <text class="level-quote" x="760" y="497" text-anchor="end" font-size="21">“it was an accident!”</text>
    </g>
    <g class="level level-vulnerable">
      <rect x="580" y="524" width="192" height="98" fill="url(#tierRed)"/>
      <polygon points="128,524 562,524 622,622 70,622" fill="url(#tierRed)"/>
      <polygon points="70,622 622,622 614,630 78,630" fill="#c4412b" opacity="0.7"/>
      <circle cx="174" cy="571" r="34" fill="#fff" stroke="#c23a24" stroke-width="4" role="img" aria-label="Vulnerable level icon"/>
      <text class="level-label" x="226" y="602" font-size="84">VULNERABLE</text>
      <text class="level-quote" x="760" y="561" text-anchor="end" font-size="17">Toxic / No care</text>
      <text class="level-quote" x="760" y="583" text-anchor="end" font-size="17">culture “accidents</text>
      <text class="level-quote" x="760" y="605" text-anchor="end" font-size="17">happen”</text>
    </g>

    <!-- step-up brackets -->
    <g class="brackets" stroke="var(--bracket)" stroke-width="3" fill="none">
      <polyline points="792,180 827,180 827,262 792,262"/>
      <polyline points="827,262 827,376 792,376"/>
      <polyline points="827,376 827,490 792,490"/>
      <polyline points="827,490 827,582 780,582"/>
    </g>
    <g class="bracket-heads" fill="var(--bracket)">
      <polygon points="782,180 794,173 794,187"/>
      <polygon points="782,262 794,255 794,269"/>
      <polygon points="782,376 794,369 794,383"/>
      <polygon points="782,490 794,483 794,497"/>
    </g>
    <text class="side-note" x="846" y="177">Develop</text>
    <text class="side-note" x="846" y="199">consistency &amp; fight</text>
    <text class="side-note" x="846" y="221">complacency</text>
    <text class="side-note" x="846" y="287">All team members</text>
    <text class="side-note" x="846" y="309">engaged &amp; all risks</text>
    <text class="side-note" x="846" y="331">controlled</text>
    <text class="side-note" x="846" y="405">Standardise</text>
    <text class="side-note" x="846" y="427">processes &amp; gain</text>
    <text class="side-note" x="846" y="449">commitment</text>
    <text class="side-note" x="846" y="526">Wake</text>
    <text class="side-note" x="846" y="548">management &amp;</text>
    <text class="side-note" x="846" y="570">control high risks</text>

    <text class="source-line" x="497" y="680" text-anchor="middle" textLength="905" lengthAdjust="spacingAndGlyphs">BASED ON THE HARLOW INSTITUTE AND DANIEL MARSH “HEADS AND HANDS” MODEL</text>
  </svg>
</section>

<!-- Back: detail per level -->
<section class="page page-detail">
  <svg viewBox="0 0 995 702" xmlns="http://www.w3.org/2000/svg">
    <defs>
      <linearGradient id="navyFill" x1="0" y1="0" x2="0" y2="1">
        <stop offset="0" stop-color="var(--navy-light)"/>
        <stop offset="0.5" stop-color="var(--navy)"/>
        <stop offset="1" stop-color="var(--navy-deep)"/>
      </linearGradient>
    </defs>
    <polygon class="navy-ground" points="0,395 995,205 995,702 0,702" fill="url(#navyFill)"/>
    <polyline class="progress-arrow" points="0,385 980,218" stroke="#6b9bd8" stroke-width="8" fill="none"/>
    <polygon points="990,215 960,206 968,232" fill="#6b9bd8"/>

    <g class="column-rules" stroke="#c9ccd3" stroke-width="1.5">
      <line x1="228" y1="22" x2="228" y2="290"/>
      <line x1="420" y1="22" x2="420" y2="255"/>
      <line x1="600" y1="22" x2="600" y2="215"/>
      <line x1="778" y1="22" x2="778" y2="190"/>
    </g>

    <g class="badge">
      <polygon points="47,368 157,368 157,396 142,410 62,410 47,396" fill="var(--orange)"/>
      <polygon points="47,364 157,364 157,390 142,402 62,402 47,390" fill="#fff"/>
      <circle cx="102" cy="335" r="34" fill="#fff" stroke="var(--red)" stroke-width="3"/>
      <circle cx="102" cy="335" r="20" fill="var(--red)" role="img" aria-label="Vulnerable level icon"/>
      <text class="badge-label" x="102" y="388" text-anchor="middle">VULNERABLE</text>
    </g>
    <g class="badge">
      <polygon points="254,326 364,326 364,354 349,368 269,368 254,354" fill="var(--orange)"/>
      <polygon points="254,322 364,322 364,348 349,360 269,360 254,348" fill="#fff"/>
      <circle cx="309" cy="290" r="34" fill="#fff" stroke="var(--red)" stroke-width="3"/>
      <circle cx="309" cy="290" r="20" fill="var(--red)" role="img" aria-label="Reactive level icon"/>
      <text class="badge-label" x="309" y="346" text-anchor="middle">REACTIVE</text>
    </g>
    <g class="badge">
      <polygon points="449,298 559,298 559,326 544,340 464,340 449,326" fill="var(--orange)"/>
      <polygon points="449,294 559,294 559,320 544,332 464,332 449,320" fill="#fff"/>
      <circle cx="504" cy="268" r="34" fill="#fff" stroke="var(--red)" stroke-width="3"/>
      <circle cx="504" cy="268" r="20" fill="var(--red)" role="img" aria-label="Compliant level icon"/>
      <text class="badge-label" x="504" y="318" text-anchor="middle">COMPLIANT</text>
    </g>
    <g class="badge">
      <polygon points="629,278 739,278 739,306 724,320 644,320 629,306" fill="var(--orange)"/>
      <polygon points="629,274 739,274 739,300 724,312 644,312 629,300" fill="#fff"/>
      <circle cx="684" cy="238" r="34" fill="#fff" stroke="var(--red)" stroke-width="3"/>
      <circle cx="684" cy="238" r="20" fill="var(--red)" role="img" aria-label="Proactive level icon"/>
      <text class="badge-label" x="684" y="298" text-anchor="middle">PROACTIVE</text>
    </g>
    <g class="badge">
      <polygon points="813,247 923,247 923,275 908,289 828,289 813,275" fill="var(--orange)"/>
      <polygon points="813,243 923,243 923,269 908,281 828,281 813,269" fill="#fff"/>
      <circle cx="868" cy="210" r="34" fill="#fff" stroke="var(--red)" stroke-width="3"/>
      <circle cx="868" cy="210" r="20" fill="var(--red)" role="img" aria-label="Resilient level icon"/>
      <text class="badge-label" x="868" y="267" text-anchor="middle">RESILIENT</text>
    </g>
  </svg>

  <!-- culture descriptions -->
  <div class="culture-col" style="left:32px;">
    <h3>Toxic / No care culture</h3>
    <ul class="traits">
      <li>Apathy / resistance</li>
      <li>Near misses not considered</li>
      <li>Negligence</li>
      <li>Dishonesty</li>
      <li>Hiding of incidents</li>
      <li>Serious injury/health risks are unseen or ignored</li>
      <li>Unfair disciplinary actions</li>
    </ul>
    <ul>
      <li>No or little training</li>
      <li>Poor or no communication</li>
      <li>Production at almost any cost</li>
      <li>“Just get it done” attitude or blatantly unsafe</li>
    </ul>
  </div>
  <div class="outcome" style="left:32px; top:196px; width:120px;">Accept that incidents happen</div>

  <div class="culture-col" style="left:171px;">
    <h3>Blame culture</h3>
    <ul class="traits">
      <li class="lead">Dependent on natural instincts</li>
      <li>Accept need to care</li>
      <li>Some near miss reporting</li>
      <li>Some window dressing e.g. pre-inspection cleanups and light duty</li>
      <li>Disciplinary action</li>
    </ul>
    <ul>
      <li>Minimum / inconsistent training</li>
      <li>Some communication on a need to know basis</li>
    </ul>
  </div>
  <div class="outcome" style="left:171px; top:171px; width:110px;">Prevent a similar incident</div>

  <div class="culture-col" style="left:309px;">
    <h3>Compliance culture</h3>
    <ul class="traits">
      <li class="lead">Supervision dependent</li>
      <li>Some participation</li>
      <li>Near miss discussions</li>
    </ul>
    <ul>
      <li>Acceptable training / awareness</li>
      <li>Established and good communication channels</li>
      <li>Regular people involvement and focus</li>
    </ul>
  </div>
  <div class="outcome" style="left:309px; top:132px; width:111px;">Prevent incidents before they occur</div>

  <div class="culture-col" style="left:439px;">
    <h3>Independent &amp; personal ownership culture</h3>
    <ul class="traits">
      <li>Involvement at all levels</li>
      <li>Near miss involvement</li>
    </ul>
    <ul>
      <li>High level of training / awareness</li>
      <li>Communication at a high level hiding nothing</li>
    </ul>
  </div>
  <div class="outcome" style="left:442px; top:118px; width:108px;">Improve the systems</div>

  <div class="culture-col" style="left:566px;">
    <h3>Interdependent teams culture</h3>
    <ul style="margin-bottom:4px;">
      <li>Way of life</li>
    </ul>
    <ul class="traits">
      <li>Comes natural</li>
      <li>Personal involvement by all to manage risks well and prevent incidents</li>
      <li>Authentic communication throughout culture</li>
    </ul>
  </div>
  <div class="outcome" style="left:566px; top:118px; width:110px;">Way we do business</div>

  <!-- practices per level -->
  <div class="practice-col" style="left:32px; top:316px;">
    <ul>
      <li>Reactive or unresponsive approach</li>
      <li>No OHS systems</li>
      <li>No risk assessment</li>
      <li>Legal non compliance</li>
      <li>Accept equipment / process decay</li>
      <li>Only fix when broken / unsafe repairs</li>
      <li>Reports are shelved / used irresponsibly</li>
      <li>No or poor investigation</li>
      <li>No monitoring / audits</li>
      <li>Permit non-compliance</li>
      <li>Potential illegal practices</li>
    </ul>
  </div>

  <div class="practice-col" style="left:171px; top:282px;">
    <ul>
      <li>Administrator driven</li>
      <li>Loose systems, elements of an OHS Management System</li>
      <li class="key">Reactive risk assessment and control</li>
      <li>Minimum legal compliance</li>
      <li>Apply PPE as a way of eliminating exposure</li>
      <li class="key">Incident investigation but limited analysis</li>
    </ul>
    <ul class="traits">
      <li>Focus on what happened</li>
      <li>No systems focus</li>
      <li>Human faults occur</li>
    </ul>
    <ul>
      <li>Ad hoc monitoring / audits</li>
      <li>No occupational hygiene or health initiatives</li>
      <li>Reactive medical monitoring</li>
      <li>Monitoring as per regulations</li>
    </ul>
  </div>

  <div class="practice-col" style="left:309px; top:268px;">
    <ul>
      <li>OHS coordinator driven</li>
      <li>OHS standards system and ISO 9002 or equivalent</li>
      <li class="key">Risk assessment through existing systems</li>
      <li>Total legal compliance goal</li>
      <li>Strictly enforced the use of PPE where required (knowing risk)</li>
      <li class="key">Causal incident analysis based on events potential</li>
      <li>Info sharing from events</li>
      <li>Planned occupational hygiene / environmental monitoring</li>
      <li>Periodical medical examinations</li>
      <li>Planned monitoring / audits</li>
      <li>Safety meetings and talks</li>
      <li>Some task observations</li>
    </ul>
  </div>

  <div class="practice-col" style="left:439px; top:251px;">
    <ul>
      <li>Committed leadership at all levels</li>
      <li>Line driven systems improvement</li>
      <li>ISO 14001 and ISO 45001</li>
      <li class="key">Pro-active formal risk management</li>
      <li>Beyond legal compliance</li>
      <li>Seek to actively engineer out process / equipment in adequacies</li>
      <li class="key">Incident learnings shared with all levels</li>
      <li>Well designed plans / procedures</li>
      <li class="key">Focus on adhering to site plans and procedures</li>
      <li>Integrated audits</li>
      <li>Peer evaluations and discussion</li>
    </ul>
  </div>

  <div class="practice-col" style="left:566px; top:231px;">
    <ul>
      <li>Individually internalized</li>
      <li>Inspiring genuine leadership</li>
      <li>No silo thinking or actions</li>
      <li>All staff active, positive, respected, speaking up</li>
      <li>Excellent equipment, ultraorganised</li>
      <li>Integrated management systems</li>
      <li class="key">Risk management cycle integrated into all systems</li>
      <li>Self regulating style</li>
      <li class="key">Eliminate &amp; prevent problems before they occur</li>
      <li>All threats considered in decision making</li>
      <li class="key">Continually improving through external evaluation / auditing</li>
      <li>Multiple positive performance indicators drive PDCA cycle</li>
    </ul>
  </div>
</section>

</body>
</html>
```